Tall Cedar Builders Business Card

I'm looking for a business card design for a start-up Handyman/Construction Company. The organization will double as a ministry to the homeless, hoping to create job opportunity and training to the homeless, providing a pathway back to being "homed". I'm looking for a simple to "seeming" simple design. Open to all thoughts.

Industry/Entity Type

Ministry

Requirements
Must have
• Logo (Attached), Name, Phone, Email and Address. Note - "*Registered and Insured".

```html
<!DOCTYPE html>
<html lang="en">
<head>
<meta charset="utf-8">
<title>Tall Cedar Builders Business Card</title>
<link rel="stylesheet" href="https://fonts.googleapis.com/css2?family=Arimo:wght@400;700&display=swap">
<style>
  :root {
    --page: #ecebe8;
    --card: #ffffff;
    --card-edge: #dcdcdc;
    --slate: #4d5873;
    --purple: #8b3f9e;
    --ink: #3f4450;
    --muted: #6b6f78;
  }
  * { box-sizing: border-box; margin: 0; padding: 0; }
  html, body {
    width: 1200px;
    height: 1000px;
    overflow: hidden;
    background: var(--page);
    font-family: "Arimo", Arial, sans-serif;
  }
  .sheet {
    position: relative;
    width: 1200px;
    height: 1000px;
  }
  .card {
    position: absolute;
    left: 250px;
    width: 700px;
    height: 400px;
    background: var(--card);
    border: 1px solid var(--card-edge);
    border-radius: 28px;
    box-shadow: 0 6px 18px rgba(0, 0, 0, 0.12);
  }
  .card--front { top: 70px; }
  .card--back { top: 530px; }

  .brand {
    position: absolute;
    left: 60px;
    bottom: 56px;
    display: flex;
    align-items: center;
    gap: 14px;
  }
  .brand-mark {
    width: 22px;
    height: 22px;
    flex: none;
    background: var(--purple);
  }
  .brand-name {
    color: var(--slate);
    font-weight: 700;
    font-size: 40px;
    letter-spacing: 0.5px;
    white-space: nowrap;
  }

  .person-name {
    position: absolute;
    left: 250px;
    top: 80px;
    color: var(--purple);
    font-weight: 700;
    font-size: 32px;
  }
  .contact-list {
    position: absolute;
    left: 250px;
    top: 190px;
    list-style: none;
    color: var(--ink);
    font-size: 15px;
  }
  .contact-list li {
    display: flex;
    align-items: center;
    gap: 10px;
    margin-bottom: 10px;
  }
  .contact-icon {
    width: 14px;
    height: 14px;
    flex: none;
    color: var(--purple);
  }
  .contact-at {
    width: 14px;
    color: var(--purple);
    font-weight: 700;
    font-size: 15px;
    text-align: center;
  }
  .note {
    position: absolute;
    right: 60px;
    bottom: 50px;
    color: var(--muted);
    font-size: 13px;
  }
</style>
</head>
<body>
<main class="sheet">
  <section class="card card--front" aria-label="Card front">
    <div class="brand">
      <span class="brand-mark" aria-hidden="true"></span>
      <p class="brand-name">Tall Cedar Builders LLC</p>
    </div>
  </section>

  <section class="card card--back" aria-label="Card back">
    <h1 class="person-name">Person Name</h1>
    <ul class="contact-list">
      <li>
        <svg class="contact-icon" viewBox="0 0 14 14" aria-hidden="true">
          <path d="M7 1 L13 7 H9.5 V13 H4.5 V7 H1 Z" fill="currentColor"/>
        </svg>
        <span>Address address address</span>
      </li>
      <li>
        <svg class="contact-icon" viewBox="0 0 14 14" aria-hidden="true">
          <path d="M3 1.5 L5.5 1 L6.5 4.2 L4.8 5.3 C5.6 7 7 8.4 8.7 9.2 L9.8 7.5 L13 8.5 L12.5 11 C12.3 12.2 11.2 13 10 12.8 C5.5 12 2 8.5 1.2 4 C1 2.8 1.8 1.7 3 1.5 Z" fill="currentColor"/>
        </svg>
        <span>0123456789 10</span>
      </li>
      <li>
        <span class="contact-at" aria-hidden="true">@</span>
        <span>xxxxxxxxx@xxxxx.xxx</span>
      </li>
    </ul>
    <p class="note">Note: "Registered and Insured"</p>
  </section>
</main>
</body>
</html>
```